Business Card for Luxury Hospitality Industry Career Seeker

Need something Simple, Punctual, and Elegant.

Project goal is to update phone number, layout, and wording

I look forward to working with you to create a business card I can give to managers and employers in the Luxury Hospitality industry. I want to advance a career in this industry handing out cards to managers and directors on my way up.
Updates

Updated graphics preferences in brief - would like my name flanked by small Oak, Lantern, & Key and have the Halvern 5 Star logo on the back Added Saturday, January 14, 2017

Updated Brief:-Some wording has been removed-Card Front should be more simple and tidy now-Card Back word choice & flow is improved Added Sunday, January 15, 2017

Target Market(s)

Luxury Hospitality Industry Employers and Managers

Industry/Entity Type

Hospitality

Contact Information for Business Card

(Card Front)
Dorian P. Keswick (flanked by small Oak, Lantern & Key graphic)
Luxury Hospitality
555-318-0147
fernpathmail@quillbox.net
tallyroster.net/in/dorian-keswick-rvfx-civ
My Experience = Our Success

(Card Back)
Graphic of: Halvern 5 Star logo and maybe QRT 5 Diamond Logo too
8 years military supply, logistics, & administrative experience
2 years intensive recruiting, marketing, and sales expertise
Adept problem solving, planning and management skills
5 Star, 5 Daimond, Luxury Hotels & Hospitality Rooms & Revenue

Requirements
Must have
• Name
• Phone Number
• Email Address
• Tally Roster Address
• Slogan (My Experience = Our Success)
• Graphic on back: Halvern 5 Star logo
• Qualification Remarks
• Catchy logo
Nice to have
• Background that makes a viewer think Luxury Hospitality Experience and/or World Experience
• Color combinations I've seen & liked are black & yellow, black & white, and blue & white

```html
<!DOCTYPE html>
<html lang="en">
<head>
<meta charset="utf-8">
<title>Dorian P. Keswick — Luxury Hospitality Business Card</title>
<link rel="stylesheet" href="https://fonts.googleapis.com/css2?family=Open+Sans:wght@400;600&family=Tinos:wght@700&display=swap">
<style>
  :root {
    --stage: #d9dbda;
    --card: #0a0a0a;
    --card-edge: #1c1c1c;
    --gold: #f0cf1e;
    --gold-deep: #b8960e;
    --gold-soft: #d9b81a;
  }
  * { margin: 0; padding: 0; box-sizing: border-box; }
  html, body { width: 1200px; height: 900px; overflow: hidden; }
  body {
    background: var(--stage);
    position: relative;
    font-family: "Open Sans", Arial, sans-serif;
    color: var(--gold);
  }
  .card {
    position: absolute;
    width: 456px;
    height: 300px;
    background: linear-gradient(160deg, var(--card-edge), var(--card) 45%);
    border-radius: 12px;
    box-shadow: 0 10px 24px rgba(0,0,0,.35);
    overflow: hidden;
  }
  /* Back of card */
  .card-back { left: 282px; top: 165px; }
  .rule { position: absolute; height: 3px; background: var(--gold); }
  .card-back .rule-top { left: 38px; right: 66px; top: 34px; }
  .card-back .rule-mid { left: 52px; right: 54px; top: 126px; }
  .card-back .rule-bottom { left: 52px; right: 100px; top: 170px; }
  .qualifications {
    position: absolute; left: 40px; top: 44px;
    list-style: none; font-size: 12.2px; line-height: 18px;
  }
  .qualifications li { display: flex; align-items: center; gap: 6px; white-space: nowrap; }
  .qualifications svg { flex: none; }
  .qualifications li:last-child { margin-top: 8px; }
  .hotel-mark {
    position: absolute; left: 170px; top: 180px; width: 118px; height: 96px;
    background: linear-gradient(180deg, var(--gold), var(--gold-deep));
    border-radius: 6px 6px 40px 40px;
  }
  /* Front of card */
  .card-front { left: 470px; top: 458px; }
  .crest {
    position: absolute; left: 28px; top: 92px; width: 62px;
    font-size: 10px; font-weight: 600; line-height: 12px; color: var(--gold);
  }
  .flourish {
    position: absolute; left: 158px; top: 84px; width: 124px; height: 8px;
    background: linear-gradient(90deg, transparent, var(--gold) 30%, var(--gold) 70%, transparent);
    border-radius: 4px;
  }
  .name {
    position: absolute; left: 0; right: 0; top: 100px; text-align: center;
    font-size: 22px; font-weight: 400; letter-spacing: .2px; padding-left: 18px;
  }
  .specialty {
    position: absolute; left: 0; right: 0; top: 135px; text-align: center;
    font-family: "Tinos", "Times New Roman", serif; font-weight: 700;
    font-size: 13px; letter-spacing: 3.4px; padding-left: 24px;
  }
  .slogan {
    position: absolute; right: 26px; top: 190px;
    font-family: "Tinos", "Times New Roman", serif; font-weight: 700; font-size: 15.5px;
  }
  .card-front .rule-a { left: 0; right: 0; top: 213px; height: 2px; }
  .card-front .rule-b { left: 0; right: 0; top: 282px; height: 2px; }
  .network {
    position: absolute; right: 14px; top: 225px;
    display: flex; align-items: center; gap: 5px; font-size: 11.5px;
  }
  .network .square { width: 10px; height: 10px; background: var(--gold); }
  .contacts {
    position: absolute; left: 40px; right: 14px; top: 255px;
    display: flex; gap: 34px; font-size: 11.5px;
  }
  .contacts span { display: flex; align-items: center; gap: 6px; white-space: nowrap; }
</style>
</head>
<body>

<section class="card card-back" aria-label="Card back">
  <div class="rule rule-top"></div>
  <ul class="qualifications">
    <li><svg width="11" height="10" viewBox="0 0 11 10"><path d="M1 5l3 3 6-7" fill="none" stroke="currentColor" stroke-width="2.2"/></svg>8 years military supply, logistics, &amp; administrative experience</li>
    <li><svg width="11" height="10" viewBox="0 0 11 10"><path d="M1 5l3 3 6-7" fill="none" stroke="currentColor" stroke-width="2.2"/></svg>2 years intensive recruiting, marketing, and sales expertise</li>
    <li><svg width="11" height="10" viewBox="0 0 11 10"><path d="M1 5l3 3 6-7" fill="none" stroke="currentColor" stroke-width="2.2"/></svg>Adept problem solving, planning and management skills</li>
    <li><svg width="11" height="10" viewBox="0 0 11 10"><path d="M1 5l3 3 6-7" fill="none" stroke="currentColor" stroke-width="2.2"/></svg>5 Star, 5 Daimond, Luxury Hotels &amp; Hospitality Rooms &amp; Revenue</li>
  </ul>
  <div class="rule rule-mid"></div>
  <div class="rule rule-bottom"></div>
  <div class="hotel-mark" role="img" aria-label="Gold hotel emblem: five stars above hotel towers on a row of diamonds"></div>
</section>

<section class="card card-front" aria-label="Card front">
  <div class="crest">Oak, Lantern &amp; Key</div>
  <div class="flourish" role="img" aria-label="Gold ornamental flourish"></div>
  <h1 class="name">Dorian P. Keswick</h1>
  <p class="specialty">Luxury Hospitality</p>
  <p class="slogan">My Experience = Our Success</p>
  <div class="rule rule-a"></div>
  <div class="network"><span class="square"></span>Tally Roster /dorian-keswick</div>
  <div class="contacts">
    <span><svg width="11" height="11" viewBox="0 0 24 24"><path fill="currentColor" d="M6.6 10.8a15 15 0 006.6 6.6l2.2-2.2a1 1 0 011-.25 11.4 11.4 0 003.6.57 1 1 0 011 1V20a1 1 0 01-1 1A17 17 0 013 4a1 1 0 011-1h3.5a1 1 0 011 1c0 1.25.2 2.45.57 3.57a1 1 0 01-.25 1z"/></svg>555-318-0147</span>
    <span><svg width="13" height="10" viewBox="0 0 13 10"><rect width="13" height="10" fill="currentColor"/><path d="M0 0l6.5 5L13 0" fill="none" stroke="#0a0a0a" stroke-width="1.3"/></svg>fernpathmail@quillbox.net</span>
  </div>
  <div class="rule rule-b"></div>
</section>

</body>
</html>
```